Birchmoor Yard Care_2015 New Cards_V1

We need an enhanced business card from what we have today. We are a Landscaping company and we have an existing Logo and text info that we would like to include.
Text to include:
In business for over 20 years,Fully Insured, Weekly Lawn Maintenance, Spring & Fall Clean-up, Todd Pierson, 203-555-0147, www.birchmooryardcarect.example, Visit our Website for additional Lawn Care Services or email directly at TODD@BIRCHMOORYARDCARE.EXAMPLE, We appreciate your business.
We want full color background and we will want to take this design and work with a printer that does high graphic silk screen cards. The colors we have thought about are Black, with our Green Logo, with Gold Text...we are open to different colors, we just want the card to wow!

Target Market(s)

Lawn Care Maintenance

Industry/Entity Type

Lawn Care

Contact Information for Business Card

Text to include:
In business for over 20 years, Fully Insured, Weekly Lawn Maintenance, Spring & Fall Clean-up, Todd Pierson, 203-555-0147, www.birchmooryardcarect.example, Visit our Website for additional Lawn Care Services or email directly at TODD@BIRCHMOORYARDCARE.EXAMPLE, We appreciate your business.

Requirements
Must have
• Logo, text details about how to reach us, standard size business cards that go horizontal.
Nice to have
• background colors, background designs, raised embossed lettering, rounded corners(2 or 4),

```html
<!DOCTYPE html>
<html lang="en">
<head>
<meta charset="utf-8">
<title>Birchmoor Yard Care – Business Cards</title>
<link href="https://fonts.googleapis.com/css2?family=Open+Sans:wght@400;600;700&display=swap" rel="stylesheet">
<style>
  :root {
    --page-bg: #e9e8e4;
    --card-bg: #f7f7f5;
    --card-edge: #d9d9d6;
    --brand-green: #1f5a2a;
    --text-green: #24582c;
    --rule: #6f8f73;
  }
  * { box-sizing: border-box; margin: 0; padding: 0; }
  html, body { width: 1200px; height: 780px; overflow: hidden; }
  body {
    background: var(--page-bg);
    font-family: "Open Sans", Arial, sans-serif;
    color: var(--text-green);
    display: flex;
    align-items: center;
    justify-content: center;
    gap: 34px;
  }
  .card {
    width: 560px;
    height: 320px;
    background: linear-gradient(160deg, #ffffff 0%, var(--card-bg) 55%, #ebebe8 100%);
    border-radius: 20px;
    box-shadow: 0 2px 0 var(--card-edge), 0 4px 0 #cfcfcc, 0 12px 24px rgba(0,0,0,.14);
    position: relative;
    overflow: hidden;
  }
  .brand-name {
    font-weight: 700;
    color: var(--brand-green);
    line-height: 1.08;
  }
  .brand-dot {
    width: 14px; height: 14px; border-radius: 50%;
    background: var(--brand-green);
    flex: none;
  }

  /* Front */
  .card-front {
    display: flex;
    align-items: center;
    padding: 0 30px 0 36px;
  }
  .front-brand {
    width: 206px;
    display: flex;
    align-items: center;
    gap: 12px;
  }
  .front-brand .brand-name { font-size: 30px; }
  .front-divider {
    width: 1px;
    height: 150px;
    background: var(--rule);
    margin: 0 20px 0 14px;
    flex: none;
  }
  .front-info { flex: 1; min-width: 0; }
  .person-name {
    font-size: 24px;
    font-weight: 700;
    margin-bottom: 14px;
    padding-bottom: 12px;
    border-bottom: 1px solid var(--rule);
  }
  .contact-list { list-style: none; }
  .contact-list li {
    display: flex;
    align-items: center;
    gap: 8px;
    font-size: 13.5px;
    line-height: 1;
    margin-bottom: 10px;
    white-space: nowrap;
  }
  .contact-icon {
    width: 16px; height: 16px;
    border-radius: 3px;
    background: var(--brand-green);
    display: flex; align-items: center; justify-content: center;
    flex: none;
  }

  /* Back */
  .card-back { padding: 32px 44px; }
  .back-brand {
    display: flex;
    align-items: center;
    gap: 12px;
    padding-bottom: 14px;
    border-bottom: 1px solid var(--rule);
  }
  .back-brand .brand-name { font-size: 34px; }
  .service-list {
    list-style: none;
    margin-top: 14px;
  }
  .service-list li {
    display: flex;
    align-items: center;
    gap: 10px;
    font-size: 17px;
    line-height: 24px;
  }
  .service-list li::before {
    content: "";
    width: 8px; height: 8px;
    background: var(--brand-green);
    transform: rotate(45deg);
    flex: none;
  }
</style>
</head>
<body>

  <section class="card card-front" aria-label="Business card front">
    <div class="front-brand">
      <span class="brand-dot"></span>
      <span class="brand-name">Birchmoor Yard Care</span>
    </div>
    <div class="front-divider"></div>
    <div class="front-info">
      <h1 class="person-name">Todd Pierson</h1>
      <ul class="contact-list">
        <li>
          <span class="contact-icon">
            <svg width="10" height="10" viewBox="0 0 10 10"><path d="M2 1l2 2-1 1c.6 1.3 1.7 2.4 3 3l1-1 2 2-1.3 1.3C4.5 9 1 5.5.7 2.3z" fill="#fff"/></svg>
          </span>
          203-555-0147
        </li>
        <li>
          <span class="contact-icon">
            <svg width="11" height="9" viewBox="0 0 11 9"><rect x=".5" y=".5" width="10" height="8" fill="none" stroke="#fff"/><path d="M.5.5l5 4.5 5-4.5" fill="none" stroke="#fff"/></svg>
          </span>
          todd@birchmooryardcare.example
        </li>
        <li>
          <span class="contact-icon">
            <svg width="11" height="11" viewBox="0 0 11 11"><circle cx="5.5" cy="5.5" r="4.8" fill="none" stroke="#fff"/><ellipse cx="5.5" cy="5.5" rx="2" ry="4.8" fill="none" stroke="#fff"/><path d="M.7 5.5h9.6" stroke="#fff"/></svg>
          </span>
          www.birchmooryardcarect.example
        </li>
      </ul>
    </div>
  </section>

  <section class="card card-back" aria-label="Business card back">
    <div class="back-brand">
      <span class="brand-dot"></span>
      <span class="brand-name">Birchmoor Yard Care</span>
    </div>
    <ul class="service-list">
      <li>Weekly Mowing</li>
      <li>Spring &amp; Fall Clean-Ups</li>
      <li>Mulching of Flower/Plant Beds</li>
      <li>Edging</li>
      <li>Hedge &amp; Shrub Trimming</li>
      <li>Tree &amp; Shrub Plantings</li>
      <li>Light Tree Triming</li>
    </ul>
  </section>

</body>
</html>
```